Company Mission & Values Poster

I'd like an A2 Portrait Poster displaying our company's Mission & Values.
See our website for our logo, fonts, mission & values.
https://talvendo.com.au/

Our Mission: Creating homes for abundant life
Values: Love, Thinking, Team, Zoe.

Some ideas to consider:
Mission as the Headline then
A logo for each of the 4 Values and the words

Target Market(s)

Myself & my team

Industry/Entity Type

Real Estate

Font styles to use
Other font styles liked:
• Company fonts as seen on our website

```html
<!DOCTYPE html>
<html lang="en">
<head>
<meta charset="utf-8">
<title>Talvendo – Mission &amp; Values</title>
<link rel="stylesheet" href="https://fonts.googleapis.com/css2?family=Cormorant+Garamond:wght@600&family=Merriweather+Sans:wght@500&family=Poppins:wght@400&display=swap">
<style>
  :root {
    --green: #0a3a33;
    --sage: #a3b5b1;
    --tint: #dfe7e5;
    --paper: #f7f7f7;
    --backdrop: #e9e9e7;
    --white: #ffffff;
  }
  * { box-sizing: border-box; margin: 0; padding: 0; }
  html, body { width: 1200px; height: 1200px; overflow: hidden; background: var(--backdrop); }
  .poster {
    position: absolute; left: 191px; top: 20px;
    width: 818px; height: 1160px;
    background: var(--paper); color: var(--green);
    font-family: "Poppins", sans-serif;
  }
  .brand-name {
    position: absolute; top: 36px; left: 0; width: 100%;
    text-align: center;
    font-family: "Cormorant Garamond", serif; font-weight: 600;
    font-size: 60px; letter-spacing: 6px; line-height: 1;
  }
  .rule { position: absolute; left: 0; width: 100%; height: 1px; background: var(--green); }
  .rule-top { top: 134px; }
  .rule-mid { top: 313px; }
  .tab {
    position: absolute; left: 277px; width: 261px; height: 39px;
    background: var(--green); color: var(--white);
    font-size: 15px; line-height: 39px; text-align: center; letter-spacing: .3px;
  }
  .tab-mission { top: 134px; }
  .tab-values { top: 314px; }
  .headline {
    position: absolute; top: 182px; left: 0; width: 100%;
    text-align: center;
    font-family: "Merriweather Sans", sans-serif; font-weight: 500;
    font-size: 40px; line-height: 1.2;
  }
  .mission-text {
    position: absolute; top: 237px; left: 80px; width: 658px;
    text-align: center; font-size: 12.6px; line-height: 17.8px;
  }
  .value-card {
    position: absolute; width: 335px; height: 335px;
    border: 1.3px solid var(--green); border-radius: 66px;
  }
  .card-love { left: 65px; top: 377px; }
  .card-thinking { left: 417px; top: 377px; }
  .card-zoe { left: 65px; top: 733px; }
  .card-team { left: 417px; top: 733px; }
  .value-text {
    position: absolute; font-size: 12.6px; line-height: 17.8px; width: 245px;
  }
  .value-text.left { left: 114px; }
  .value-text.right { left: 456px; text-align: right; }
  .value-text.upper { top: 416px; }
  .value-text.lower { top: 926px; }
  .divider { position: absolute; width: 109px; height: 1.3px; background: var(--green); }
  .divider.left { left: 119px; }
  .divider.right { left: 592px; }
  .divider.upper { top: 549px; }
  .divider.lower { top: 902px; }
  .icon-slot {
    position: absolute; width: 80px; height: 76px;
    background: var(--tint); border-radius: 14px;
  }
  .icon-love { left: 117px; top: 588px; }
  .icon-thinking { left: 622px; top: 588px; }
  .icon-zoe { left: 117px; top: 786px; }
  .icon-team { left: 622px; top: 786px; }
  .values-wheel { position: absolute; left: 0; top: 0; width: 818px; height: 1160px; }
  .wheel-label {
    font-family: "Cormorant Garamond", serif; font-weight: 600;
    font-size: 30px; fill: var(--white); letter-spacing: 1px;
  }
  .footer {
    position: absolute; left: 0; bottom: 0; width: 100%; height: 61px;
    background: var(--green); color: var(--white);
    font-family: "Cormorant Garamond", serif; font-weight: 600;
    font-size: 23px; letter-spacing: 1px; line-height: 61px; text-align: center;
  }
</style>
</head>
<body>
<main class="poster">
  <h1 class="brand-name">TALVENDO</h1>

  <div class="rule rule-top"></div>
  <div class="tab tab-mission">OUR MISSION</div>
  <h2 class="headline">Creating homes for abundant life.</h2>
  <p class="mission-text">We wholeheartedly believe that home is an extraordinary place: a haven where life unfolds in all its glory. Where we find solace, make cherished memories with loved ones, and savour the natural beauty that surrounds us.</p>

  <div class="rule rule-mid"></div>
  <div class="tab tab-values">OUR VALUES</div>

  <div class="value-card card-love"></div>
  <div class="value-card card-thinking"></div>
  <div class="value-card card-zoe"></div>
  <div class="value-card card-team"></div>

  <p class="value-text left upper">Our mission is founded in our love and respect for people - those we develop for, those in our teams and those in the communities we create and operate within.</p>
  <p class="value-text right upper">We believe in the power of thinking. Our rigorous and creative processes create beautifully considered solutions for our purchasers, the communities we develop within and the environment.</p>
  <p class="value-text left lower">Our mission is to create places for 'Zoe' - the Greek word for abundant life. We do this through exquisite design, quality construction and celebrating nature.</p>
  <p class="value-text right lower">Property development is a team sport. We surround ourselves with the best designers and advisers. We strive to create an environment that allows them to do their best work and love doing it.</p>

  <div class="divider left upper"></div>
  <div class="divider right upper"></div>
  <div class="divider left lower"></div>
  <div class="divider right lower"></div>

  <div class="icon-slot icon-love" role="img" aria-label="Icon of a heart embraced by arms, for Love"></div>
  <div class="icon-slot icon-thinking" role="img" aria-label="Icon of a brain inside a light bulb, for Thinking"></div>
  <div class="icon-slot icon-zoe" role="img" aria-label="Icon of a joyful figure with raised arms, for Zoe"></div>
  <div class="icon-slot icon-team" role="img" aria-label="Icon of hands holding a group of people, for Team"></div>

  <svg class="values-wheel" viewBox="0 0 818 1160" aria-hidden="true">
    <defs>
      <path id="arc-love" d="M 249 723 A 156 156 0 0 1 405 567"/>
      <path id="arc-thinking" d="M 405 567 A 156 156 0 0 1 561 723"/>
      <path id="arc-zoe" d="M 231 723 A 174 174 0 0 0 405 897"/>
      <path id="arc-team" d="M 405 897 A 174 174 0 0 0 579 723"/>
    </defs>
    <circle cx="405" cy="723" r="206" fill="var(--sage)"/>
    <circle cx="405" cy="723" r="197" fill="var(--green)"/>
    <circle cx="405" cy="723" r="133" fill="var(--white)"/>
    <circle cx="405" cy="723" r="124" fill="var(--sage)"/>
    <circle cx="405" cy="723" r="115" fill="var(--green)"/>
    <rect x="398" y="510" width="14" height="80" fill="var(--white)"/>
    <rect x="398" y="856" width="14" height="80" fill="var(--white)"/>
    <rect x="190" y="716" width="82" height="14" fill="var(--white)"/>
    <rect x="538" y="716" width="82" height="14" fill="var(--white)"/>
    <text class="wheel-label"><textPath href="#arc-love" startOffset="50%" text-anchor="middle">Love</textPath></text>
    <text class="wheel-label"><textPath href="#arc-thinking" startOffset="50%" text-anchor="middle">Thinking</textPath></text>
    <text class="wheel-label"><textPath href="#arc-zoe" startOffset="50%" text-anchor="middle">Zoe</textPath></text>
    <text class="wheel-label"><textPath href="#arc-team" startOffset="50%" text-anchor="middle">Team</textPath></text>
  </svg>

  <footer class="footer">www.talvendo.com.au</footer>
</main>
</body>
</html>
```